Brightwell Commercial Cleaning - Company OverView

I require a 3 page, A4 company folding proschure. I would like to convey a eco frienddly and professional service. Text and images can be found on our company web page www.brightwellcleaning.com.au however we may need some more eco friendly images to convey the right message

The broschure must highlight our companys ISO certification. We are a professional service targeting the corporate industry.

I have hi res images to send and also endorsement and certification logos to send through.

Designer may need to suppl;y some contact and images.

We would like to work with someoe frquently
Updates

HI TEAM, I AM SORRY FOR ANY CONFUSION. I HAVE JUST HAD INSTRUCTIONS THAT THE BROSCHURE WILL NEED TO BE AN A3 SIZE BUT DESIGNED WITH 2 A4 PAGES FRONT AND BACK. SORRY FOR ANY INCONVENIENCE

Target Market(s)

* Corporate
* Professional

Industry/Entity Type

Professional Service

Requirements
Must have
• * Environmental Feel
* Strong Prescense
* Must be CLEAN
* Have 6 A4 pages (Must be a 3 page a4 broschure, Double sided).
Should not have
• * Busy Text
* Old Font

```html
<!DOCTYPE html>
<html lang="en">
<head>
<meta charset="utf-8">
<title>Brightwell Commercial Cleaning – Company Overview</title>
<link href="https://fonts.googleapis.com/css2?family=Lora:ital,wght@1,400;1,700&display=swap" rel="stylesheet">
<style>
  :root {
    --heading-blue: #2c3f8e;
    --body-text: #3a3a3a;
    --swoosh-deep: #0a67a8;
    --swoosh-light: #23a6dc;
    --band-grey: #e1e2e4;
    --paper: #ffffff;
    --badge-green: #2f7a3c;
    --badge-red: #d2262f;
  }
  html, body { margin: 0; padding: 0; overflow: hidden; background: var(--paper); }
  .spread {
    position: relative; width: 1200px; height: 849px; overflow: hidden;
    background: var(--paper);
    font-family: "Lora", Georgia, serif; font-style: italic; color: var(--body-text);
  }
  .backdrop { position: absolute; inset: 0; }
  .column { position: absolute; }
  .column--left { left: 152px; top: 118px; width: 430px; }
  .column--right { left: 647px; top: 118px; width: 520px; }
  .section-title {
    margin: 0 0 6px; font-weight: 700; font-size: 17px; letter-spacing: 1px;
    color: var(--heading-blue); text-transform: uppercase;
  }
  .body-copy { margin: 0; font-size: 13.2px; line-height: 24.3px; }
  .sub-title { margin: 22px 0 4px; font-size: 15px; font-weight: 400; }
  .service-list, .principle-list { list-style: none; margin: 0; padding: 0; font-size: 13.2px; line-height: 24.3px; }
  .service-list li, .principle-list li { position: relative; padding-left: 21px; }
  .service-list li::before, .principle-list li::before {
    content: "•"; position: absolute; left: 2px; font-size: 11px;
  }
  .principle-list { margin-left: 20px; }
  .integrity { margin-top: 28px; }
  .brand-name {
    position: absolute; left: 398px; top: 612px;
    font-size: 34px; font-weight: 700; color: var(--heading-blue);
  }
</style>
</head>
<body>
<div class="spread">
  <svg class="backdrop" width="1200" height="849" viewBox="0 0 1200 849" aria-hidden="false">
    <defs>
      <linearGradient id="swooshBlue" x1="0" y1="0" x2="1" y2="1">
        <stop offset="0" stop-color="var(--swoosh-deep)"/>
        <stop offset="1" stop-color="var(--swoosh-light)"/>
      </linearGradient>
      <linearGradient id="bandGrey" x1="1" y1="0" x2="0" y2="1">
        <stop offset="0" stop-color="#f4f4f5"/>
        <stop offset="1" stop-color="var(--band-grey)"/>
      </linearGradient>
      <clipPath id="photoStrip">
        <path d="M0,430 C150,680 400,720 620,706 C850,690 1050,620 1200,460 L1200,849 L0,849 Z"/>
      </clipPath>
      <linearGradient id="mallWarm" x1="0" y1="0" x2="0" y2="1"><stop offset="0" stop-color="#c9b79c"/><stop offset="1" stop-color="#e6ddd0"/></linearGradient>
      <linearGradient id="glassSky" x1="0" y1="0" x2="1" y2="1"><stop offset="0" stop-color="#d8d9db"/><stop offset="0.5" stop-color="#8fb0cc"/><stop offset="1" stop-color="#4f7fae"/></linearGradient>
      <linearGradient id="meadowSky" x1="0" y1="0" x2="0" y2="1"><stop offset="0" stop-color="#3f8fd6"/><stop offset="0.7" stop-color="#b7d8ef"/><stop offset="0.75" stop-color="#6db33f"/><stop offset="1" stop-color="#3f8a2a"/></linearGradient>
      <linearGradient id="cloudSky" x1="0" y1="0" x2="0" y2="1"><stop offset="0" stop-color="#2f86d4"/><stop offset="1" stop-color="#cfe4f4"/></linearGradient>
      <linearGradient id="treeGreen" x1="0" y1="0" x2="0" y2="1"><stop offset="0" stop-color="#6fa8d8"/><stop offset="0.35" stop-color="#5c9a34"/><stop offset="1" stop-color="#a8c64a"/></linearGradient>
      <linearGradient id="turbineSky" x1="0" y1="0" x2="0" y2="1"><stop offset="0" stop-color="#3b7fc4"/><stop offset="0.8" stop-color="#b9d3ea"/><stop offset="1" stop-color="#c9b98e"/></linearGradient>
    </defs>

    <path d="M0,0 H340 C210,40 70,140 0,255 Z" fill="url(#swooshBlue)"/>
    <path d="M350,0 L600,0 C330,60 95,215 0,440 L0,268 C75,140 205,48 350,0 Z" fill="url(#bandGrey)"/>

    <g clip-path="url(#photoStrip)">
      <rect x="0" y="400" width="120" height="449" fill="url(#mallWarm)" role="img" aria-label="Bright shopping centre interior"/>
      <rect x="120" y="400" width="232" height="449" fill="url(#glassSky)" role="img" aria-label="Polished mall floor and glass office tower"/>
      <rect x="352" y="400" width="268" height="449" fill="url(#meadowSky)" role="img" aria-label="Woman leaping with a colourful scarf over a green meadow"/>
      <rect x="620" y="400" width="226" height="449" fill="url(#cloudSky)" role="img" aria-label="Person with raised arms under a bright cloudy sky"/>
      <rect x="846" y="400" width="189" height="449" fill="url(#treeGreen)" role="img" aria-label="Large green tree in a flowering field"/>
      <rect x="1035" y="400" width="165" height="449" fill="url(#turbineSky)" role="img" aria-label="Wind turbines against a blue sky"/>
    </g>

    <path d="M0,630 C70,690 120,760 200,849 L0,849 Z" fill="var(--paper)"/>
    <circle cx="85" cy="700" r="40" fill="var(--badge-green)" role="img" aria-label="Environmental certification badge"/>
    <rect x="98" y="712" width="40" height="40" rx="4" fill="var(--badge-red)" role="img" aria-label="Certification mark"/>
    <rect x="112" y="768" width="160" height="40" rx="3" fill="#e8c9cb" role="img" aria-label="Safety award badge"/>
  </svg>

  <section class="column column--left">
    <h2 class="section-title">Services</h2>
    <p class="body-copy">Brightwell has built a process orientated service with measurable<br>quality control methods and procedures based on accountability.<br>Brightwell delivers a wide range of quality services, ensuring that the<br>management of your site is handled with competence and reliability.</p>
    <h3 class="sub-title">Services</h3>
    <ul class="service-list">
      <li>General cleaning requirements</li>
      <li>Security – 24 hour emergency contact</li>
      <li>Consumables supply and replacement</li>
      <li>Wash room services</li>
      <li>Building maintenance</li>
      <li>Scrubbing machinery</li>
      <li>Pressure washing</li>
      <li>Window cleaning</li>
      <li>Carpet care</li>
      <li>Floor maintenance</li>
      <li>Graffiti removal</li>
    </ul>
  </section>

  <section class="column column--right">
    <h2 class="section-title">Dedication to Customer Service</h2>
    <p class="body-copy">Established in 1995 and initially servicing commercial and strata offices, Brightwell<br>has progressively developed over 15 years to build a strong client network thought<br>Australia and New Zealand. Brightwell now offers the highest commercial cleaning<br>standards to commercial industry, retail and shopping centres, hotels and tertiary<br>education facilities. Our continual commitment and dedication to delivering a<br>quality service has enabled Brightwell to build a solid foundation and international<br>presence. Building relationships based on ethical conduct towards employees and<br>clientele defines our unique working environments and is a vital key to our success.</p>
    <div class="integrity">
      <h2 class="section-title">Integrity - Culture</h2>
      <p class="body-copy">Our principle to put the client first, separates us from the rest Ingrained<br>within each employee are five company principles of Brightwell.</p>
      <ul class="principle-list">
        <li>Put the client first</li>
        <li>Lead with integrity</li>
        <li>Deliver a quality service</li>
        <li>Take personal responsibility</li>
        <li>Keep balance</li>
      </ul>
      <p class="body-copy">Within these principles Brightwell has created a company that rewards<br>dependability, integrity, safety and provides the training<br>and development for all employees.</p>
    </div>
  </section>

  <div class="brand-name">Brightwell</div>
</div>
</body>
</html>
```